VELMOR Website Design

We need a website designed for our company VELMOR. We are a luxury lifestyle club that will provide benefits and services for our members. The site should be clean & sleek, preferably using black and white (or darker colors). (example sites: brastelle.com, fovix.com)

Here is a link of a sample page I did using wix. (https://dunmerel7.pagebuildr.com/mysite) This can be used to get a general idea.

Target Market(s)

Upper Middle Class in the United States

Number of Pages Required

5+ page

Font styles to use
Sans Serif
Other font styles liked:
• Arial (or other similar fonts)

Requirements
Must have
• A clean design that is eye-catching and speaks to our company.
Nice to have
• Ideas for copy.

```html
<!DOCTYPE html>
<html lang="en">
<head>
<meta charset="utf-8">
<title>VELMOR — A Members Only Lifestyle Club</title>
<link rel="stylesheet" href="https://fonts.googleapis.com/css2?family=Poppins:wght@300;400;500;600;700&display=swap">
<style>
:root{
  --ink:#000;
  --white:#fff;
  --nav-bg:rgba(20,16,14,.72);
  --hero-a:#3a2a22;
  --hero-b:#1d1a1c;
  --panel:rgba(30,26,26,.72);
  --btn-grey:#9a9a9a;
  --btn-light:#cfcfcf;
  --about-bg:#f1f1f1;
  --dark-bg:#0b0b0b;
  --interest-bg:#a9a9a9;
  --field:#8a8a8a;
  --muted:#9b9b9b;
  --footer-text:#222;
}
*{margin:0;padding:0;box-sizing:border-box}
html,body{width:754px;height:1200px;overflow:hidden}
body{font-family:"Poppins",Arial,sans-serif;background:var(--white);position:relative;color:var(--ink)}
.abs{position:absolute}

/* header */
.site-header{left:0;top:0;width:754px;height:38px;background:var(--nav-bg);z-index:3}
.brand{left:146px;top:6px;font-size:23px;font-weight:400;color:var(--white);letter-spacing:.5px}
.main-nav{left:326px;top:13px;display:flex;gap:0;font-size:10px;color:#cfcfcf}
.main-nav span{white-space:nowrap}
.main-nav .sep{margin:0 12px;color:#aaa}
.main-nav .current{color:var(--white);font-weight:500;position:relative}
.main-nav .current::after{content:"";position:absolute;left:0;right:0;top:17px;height:2px;background:#ddd}

/* hero */
.hero{left:0;top:0;width:754px;height:357px;background:linear-gradient(100deg,#26324a 0%,var(--hero-a) 35%,#5a4030 55%,var(--hero-b) 100%)}
.hero-panel{left:194px;top:131px;width:368px;height:101px;background:var(--panel)}
.hero-title{left:0;width:754px;top:146px;text-align:center;color:var(--white);font-size:21px;font-weight:600}
.hero-sub{left:0;width:754px;top:185px;text-align:center;color:var(--white);font-size:13.5px;font-weight:300}
.hero-btn{left:338px;top:217px;width:79px;height:26px;background:var(--btn-light);color:#111;font-size:8.5px;display:flex;align-items:center;justify-content:center}

/* about */
.about{left:0;top:357px;width:754px;height:264px;background:var(--about-bg)}
.about-photo{left:146px;top:390px;width:248px;height:198px;background:radial-gradient(circle at 30% 25%,#d9a55a 0%,#7a5a3a 35%,#3b2c22 75%)}
.about-kicker{left:404px;top:406px;font-size:15px;font-weight:600;line-height:1}
.about-title{left:404px;top:420px;font-size:22.5px;font-weight:600;line-height:1}
.about-copy{left:406px;top:456px;width:204px;font-size:9.3px;line-height:11.3px;font-weight:300;color:#111}
.about-copy p+p{margin-top:9px}
.btn-grey{background:var(--btn-grey);color:var(--white);font-size:9px;display:flex;align-items:center;justify-content:center}
.read-more{left:406px;top:548px;width:69px;height:18px}

/* services */
.services{left:0;top:621px;width:754px;height:342px;background:linear-gradient(90deg,#2a2a2c 0%,#141414 55%,var(--dark-bg) 100%)}
.services-title{left:0;width:754px;top:650px;text-align:center;color:var(--white);font-size:24px;font-weight:600}
.services-title .amp{color:var(--muted)}
.services-intro{left:146px;width:462px;top:684px;text-align:center;color:var(--white);font-size:9.8px;line-height:11.5px;font-weight:300}
.apply{left:342px;top:718px;width:70px;height:19px}
.service{width:103px}
.service-photo{width:103px;height:63px}
.service-label{color:var(--white);font-size:9.8px;text-align:center;margin-top:4px;font-weight:300}

/* interest */
.interest{left:0;top:963px;width:754px;height:194px;background:var(--interest-bg)}
.interest-title{left:0;width:754px;top:990px;text-align:center;color:var(--white);font-size:23px;font-weight:600}
.interest-copy{left:160px;width:434px;top:1026px;text-align:center;color:var(--white);font-size:9.8px;line-height:11.3px;font-weight:300}
.field{background:var(--field);color:#eee;font-size:9.5px;padding-left:5px;display:flex;align-items:center;font-weight:300}
.submit{left:434px;top:1081px;width:100px;height:43px;background:var(--white);font-size:9px;font-weight:600;display:flex;align-items:center;justify-content:center}

/* footer */
.footer-nav{left:146px;top:1163px;display:flex;align-items:center;font-size:9.5px;font-weight:500;color:var(--footer-text)}
.footer-nav .dot{width:3px;height:3px;border-radius:50%;background:#999;margin:0 10px}
.copyright{left:146px;top:1181px;font-size:7px;color:#555}
.social{left:494px;top:1171px;display:flex;gap:14px}
.social span{width:17px;height:17px;border-radius:50%;background:#8a8a8a;display:block}
</style>
</head>
<body>

<section class="abs hero" role="img" aria-label="Photo of members toasting with wine glasses at a dinner table"></section>
<header class="abs site-header"></header>
<div class="abs brand">VELMOR</div>
<nav class="abs main-nav">
  <span class="current">Home</span><span class="sep">|</span>
  <span>About</span><span class="sep">|</span>
  <span>Services and Benefits</span><span class="sep">|</span>
  <span>Contact</span>
</nav>
<div class="abs hero-panel"></div>
<h1 class="abs hero-title">A Members Only Lifestyle Club</h1>
<p class="abs hero-sub">BECOME A MEMBER TODAY!</p>
<div class="abs hero-btn">JOINT CLUBE</div>

<section class="abs about"></section>
<div class="abs about-photo" role="img" aria-label="Photo of a raised champagne glass at a warm-lit gathering"></div>
<div class="abs about-kicker">About</div>
<h2 class="abs about-title">VELMOR</h2>
<div class="abs about-copy">
  <p>VELMOR is a members only lifestyle club founded in order to bring the best services, experiences, and opportunities to our diverse community of members.</p>
  <p>Our members consist of creatives, athletes, artists, and other professionals.</p>
</div>
<div class="abs btn-grey read-more">READ MORE</div>

<section class="abs services" role="img" aria-label="Dark background photo of a private jet on a runway"></section>
<h2 class="abs services-title">SERVICES <span class="amp">&amp;</span> BENEFITS</h2>
<p class="abs services-intro">Built in the image of a"Multi-Family Office", VELMOR provides members with access to just about any service, experience, and event desirable.</p>
<div class="abs btn-grey apply">APPLY</div>

<div class="abs service" style="left:146px;top:762px"><div class="service-photo" role="img" aria-label="Investment chart photo" style="background:linear-gradient(135deg,#1e3d7a,#4a6fb0)"></div><div class="service-label">Investment</div></div>
<div class="abs service" style="left:267px;top:762px"><div class="service-photo" role="img" aria-label="Lawyer in suit holding a book" style="background:linear-gradient(135deg,#3a1a14,#1a1a1a)"></div><div class="service-label">Lawyer</div></div>
<div class="abs service" style="left:383px;top:762px"><div class="service-photo" role="img" aria-label="Couple celebrating a new home" style="background:linear-gradient(135deg,#2a5fa0,#9ab8d0)"></div><div class="service-label">Real Estate</div></div>
<div class="abs service" style="left:506px;top:762px"><div class="service-photo" role="img" aria-label="Concierge desk with a small frame" style="background:linear-gradient(180deg,#f4f2ee,#c9b8a4)"></div><div class="service-label">24/7 Concierge</div></div>

<div class="abs service" style="left:146px;top:857px"><div class="service-photo" role="img" aria-label="Accounting papers with a pen" style="background:linear-gradient(135deg,#e6ecf3,#8aa3c4)"></div><div class="service-label">Accounting</div></div>
<div class="abs service" style="left:267px;top:857px"><div class="service-photo" role="img" aria-label="Travellers boarding a private jet" style="background:linear-gradient(180deg,#cfd6dc,#8a8578)"></div><div class="service-label">Private Jet Travel</div></div>
<div class="abs service" style="left:383px;top:857px"><div class="service-photo" role="img" aria-label="Black and white concert crowd" style="background:linear-gradient(135deg,#d8d8d8,#2a2a2a)"></div><div class="service-label">Event Access</div></div>
<div class="abs service" style="left:506px;top:857px"><div class="service-photo" role="img" aria-label="Friends at an outdoor dinner party" style="background:linear-gradient(135deg,#5a7a3a,#b0704a)"></div><div class="service-label">Private Events</div></div>

<section class="abs interest"></section>
<h2 class="abs interest-title">INDICATION OF INTEREST</h2>
<p class="abs interest-copy">Hey - Thanks for your interest! We will begin accepting applications in 2019. In the meantime, simply fill out the indication of interest below and we will be in touch once we begin accepting applications!</p>
<div class="abs field" style="left:220px;top:1081px;width:208px;height:18px">Full Name</div>
<div class="abs field" style="left:220px;top:1106px;width:100px;height:18px">Email</div>
<div class="abs field" style="left:327px;top:1106px;width:101px;height:18px">Phone</div>
<div class="abs submit">SUBMIT</div>

<nav class="abs footer-nav">
  <span>Home</span><span class="dot"></span>
  <span>About</span><span class="dot"></span>
  <span>Services &amp; Benefits</span><span class="dot"></span>
  <span>Contact</span>
</nav>
<div class="abs copyright">Copyright © 2018 VELMOR. All Rights Reserved.</div>
<div class="abs social" aria-label="Social links"><span></span><span></span><span></span><span></span></div>

</body>
</html>
```